Information Prospectus for education sector

We need to create a 12 page information memorandum reagrding the education an industry snapshot in Australia, This will be sent to investors in Australia and overseas looking to invest into the education sector in Australia.

Target Market(s)

Investors into the education sector

Industry/Entity Type

Education

Font styles to use
Sans Serif

Colors
fbee3d
33a6d7
9bcb3c

```html
<!DOCTYPE html>
<html lang="en">
<head>
<meta charset="utf-8">
<title>International Education Industry Snapshot – Prospectus Spreads</title>
<link href="https://fonts.googleapis.com/css2?family=Oswald:wght@400;500;600;700&family=Open+Sans:wght@400;600;700;800&display=swap" rel="stylesheet">
<style>
:root{
  --blue:#33a6d7;
  --blue-deep:#1f86bd;
  --yellow:#fbee3d;
  --green:#9bcb3c;
  --stage:#444446;
  --ink:#1c1c1c;
  --paper:#ffffff;
}
*{box-sizing:border-box;margin:0;padding:0}
html,body{width:1200px;height:1200px;overflow:hidden;background:var(--stage)}
body{position:relative;font-family:"Open Sans",Arial,sans-serif;color:var(--ink)}
.page{position:absolute;width:272px;height:378px;background:var(--paper);overflow:hidden}
.c1{left:28px}.c2{left:318px}.c3{left:608px}.c4{left:898px}
.r1{top:14px}.r2{top:410px}.r3{top:806px}
.fill{position:absolute}
.head{font-family:"Oswald",Arial,sans-serif;font-weight:600;color:#fff;line-height:1.05}
.wordmark{font-family:"Open Sans",Arial,sans-serif;font-weight:700;letter-spacing:0}
.body{font-size:5px;line-height:1.45;text-align:justify}
.body p{margin-bottom:4px}
.white{color:#fff}
.footer{position:absolute;left:0;bottom:0;width:100%;height:14px;background:var(--green)}
.footer .web{position:absolute;left:12px;top:4px;font-size:4.5px;font-weight:700;color:#fff}
.footer .tab{position:absolute;right:0;top:-4px;width:48px;height:18px;background:var(--yellow);clip-path:polygon(14% 0,100% 0,100% 100%,0 100%);font-size:4.5px;font-weight:700;text-align:center;padding-top:8px;color:var(--ink)}
.bullets{list-style:none}
.bullets li{position:relative;padding-left:7px;margin-bottom:4px}
.bullets li::before{content:"";position:absolute;left:0;top:2px;width:3px;height:3px;border-radius:50%;background:var(--yellow)}
.ticks li::before{width:4px;height:2px;border-radius:0;background:none;border-left:1px solid var(--yellow);border-bottom:1px solid var(--yellow);transform:rotate(-45deg);top:1.5px}
.label-box{position:absolute;background:var(--yellow);font-weight:800;font-size:14.5px;line-height:1.25;padding:6px 6px;color:var(--ink)}

.cover{background:var(--blue)}
.cover .brand{position:absolute;left:10px;top:14px;font-size:15px;color:#fff}
.cover .title{position:absolute;left:14px;top:222px;font-size:26px;font-weight:700}
.cover .rule{position:absolute;left:14px;top:322px;width:230px;height:1px;background:#fff}
.cover .band{position:absolute;left:0;bottom:0;width:100%;height:42px;background:var(--yellow)}
.cover .band span{position:absolute;left:20px;top:15px;font-size:8.5px;font-weight:700}

.g-box{position:absolute;left:28px;top:8px;width:210px;height:140px;background:var(--green);border-radius:18px}
.b-box{position:absolute;left:35px;top:202px;width:200px;height:140px;border:5px solid var(--blue);border-radius:20px;background:var(--blue)}

.feature h4{font-size:6.5px;font-weight:700;margin-bottom:2px}
.feature{position:absolute;left:112px;width:150px}
.quote{position:absolute;left:110px;top:285px;width:155px;height:40px;border:1px solid #999;border-radius:6px;padding:5px 6px}
.quote b{display:block;font-size:9.5px;font-weight:800}
.quote span{font-size:6.5px;line-height:1.3;display:block}

.data{border-collapse:collapse;width:100%;font-size:3px}
.data th{background:#1d2b6b;color:#fff;font-weight:700;padding:.6px 1px;text-align:left}
.data td{padding:.5px 1px;border-bottom:.4px solid #bbb}
.data tr.total td{font-weight:700;border-top:.6px solid #000}

.contact h5{font-family:"Oswald",sans-serif;font-weight:500;font-size:10px;color:var(--yellow)}
.contact .role{font-family:"Oswald",sans-serif;font-size:5px;color:var(--yellow);margin-bottom:5px}
.contact .line{display:flex;align-items:center;gap:4px;font-size:4.5px;color:#fff;margin-bottom:4px}
</style>
</head>
<body>

<section class="page c1 r1 cover">
  <div class="brand wordmark">Kestrel Advisory</div>
  <div class="fill" style="left:0;top:45px;width:272px;height:170px;background:linear-gradient(135deg,#6b8fb0,#e3a35a 55%,#2d4a70)" role="img" aria-label="Hand holding a small globe wearing a graduation cap"></div>
  <div class="head title">THE INTERNATIONAL<br>EDUCATION INDUSTRY<br>SNAPSHOT</div>
  <div class="rule"></div>
  <div class="band"><span>www.kestreladvisory.com.au</span></div>
</section>

<section class="page c2 r1" style="background:var(--blue)">
  <div class="fill" style="left:0;top:0;width:272px;height:188px;background:linear-gradient(180deg,#3a3a3a,#a9a9a9 60%,#555)" role="img" aria-label="Black and white photo of an open book in a library"></div>
  <div class="body white fill" style="left:22px;top:202px;width:228px">
    <p>Kestrel Advisory is an independent and Australian owned agency providing premium specialist services to investors, buyers and sellers across the private education markets.</p>
    <p>Our team consists of people with a long-term successful career in the education industry. The team is a knowledgeable and informed group of professionals with a strong commitment and attitude which allows us to professionally drive negotiations.</p>
    <p>In the first six months of 2018, we have successfully completed many transactions in the sale of international education institutes. We currently have investment and acquisition opportunities from $1m to $15m.</p>
    <p>Throughout this presentation, prospective investors will have an insight knowledge of:</p>
    <ul class="bullets">
      <li>The outlook and growth of International Education Industry in Australia</li>
      <li>Investment opportunity of International Education Industry in Australia</li>
      <li>Investment return and risks</li>
    </ul>
  </div>
  <div class="footer"><span class="web">www.kestreladvisory.com.au</span><span class="tab">Page 2</span></div>
</section>

<section class="page c3 r1">
  <div class="fill head" style="left:0;top:0;width:272px;height:54px;background:var(--blue);text-align:center;font-size:15px;font-weight:500;padding-top:11px">International Education Industry<br>in Australia</div>
  <div class="fill" style="left:0;top:62px;width:125px;height:290px;background:linear-gradient(90deg,#1b1b1b,#8d8d8d 50%,#2a2a2a)" role="img" aria-label="Black and white photo of library bookshelves"></div>
  <div class="body fill" style="left:133px;top:68px;width:130px;font-size:4.6px">
    <p>In 2016-2017, the Education Industry generated $28.6 Billion to the Australian Economy and was the third largest source of export income for Australia after Iron and Coal. It increased 16.1% compared to 2015-2016 Financial Year which was $24.145 Billion. The growth in Education Export has been very sustainable with the average growth of 11% in the last 5 years.</p>
    <p>The higher education sector generated $19.1 billion in export income (68.1% of total on-shore earnings). The VET sector generated $4.8 billion in earnings (17.3% of total), ELICOS was $1.4 billion (5.2%); schools was $1.2 billion (4.4%); and non-award was $981 million (3.5%).</p>
  </div>
  <div class="fill" style="left:129px;top:196px;width:143px;height:146px;background:var(--green);padding:5px">
    <div style="background:#fff;height:136px;position:relative">
      <div class="fill" style="left:4px;top:4px;font-size:3.6px;width:28px">2016–17 export income by state and territory</div>
      <div class="fill" style="left:34px;top:4px;width:70px;height:54px;background:#5b4bb0;border-radius:10px 20px 8px 14px" role="img" aria-label="Map of Australian states with export income"></div>
      <div class="fill" style="left:108px;top:4px;width:24px;height:24px;border-radius:50%;border:1px solid #5b4bb0"></div>
      <div class="fill" style="left:4px;top:66px;width:128px;font-size:3.2px;line-height:1.3">
        <div style="display:flex;gap:4px;margin-bottom:4px"><span style="width:22px;height:9px;background:#5b4bb0;display:block;flex:none"></span>Education is the 3rd largest export for Australia</div>
        <div style="display:flex;gap:4px;margin-bottom:4px"><span style="width:22px;height:9px;background:#5b4bb0;display:block;flex:none"></span>International education supports 130,000 jobs nationally</div>
        <div style="display:flex;gap:4px;margin-bottom:4px"><span style="width:22px;height:9px;background:#5b4bb0;display:block;flex:none"></span>China 28% and India 11% are the largest sources of students</div>
        <div style="display:flex;gap:4px"><span style="width:22px;height:9px;background:#5b4bb0;display:block;flex:none"></span>43% of enrolments are in higher education and 26% in VET</div>
      </div>
    </div>
  </div>
  <div class="footer"><span class="web">www.kestreladvisory.com.au</span><span class="tab">Page 3</span></div>
</section>

<section class="page c4 r1">
  <div class="g-box">
    <div style="font-size:4px;text-align:center;margin-top:11px">Export income by state and territory, 2016-17</div>
    <div class="fill" style="left:22px;top:20px;width:165px;height:108px;background:#f3e6b8;border-radius:30px 50px 20px 40px" role="img" aria-label="Map of Australia showing export income by state"></div>
  </div>
  <div class="body fill" style="left:10px;top:156px;width:252px;font-size:4.2px">
    <p>The International Education Industry is non arguably one of the key forces to drive the Australian Economy for now and in the future.</p>
    <p>Australia has established itself as the global leader in the provision of international education. Its comparative strength - that is, the 'Australian Advantage' - has been integral to our performance to this point, and will be key to the sector's future successes.</p>
  </div>
  <div class="b-box">
    <div style="font-size:4px;color:#fff;text-align:center;font-weight:700;margin-top:2px">Onshore in Australia: Export income from education services</div>
    <svg class="fill" style="left:6px;top:14px" width="180" height="100" viewBox="0 0 180 100">
      <g stroke="#fff" stroke-width=".6" fill="none"><path d="M14 2V86H176"/></g>
      <g fill="#fff" font-size="3.5" font-family="Open Sans">
        <text x="2" y="4">30.0</text><text x="2" y="30">20.0</text><text x="2" y="58">10.0</text><text x="4" y="87">0.0</text>
        <rect x="26" y="38" width="7" height="48"/><rect x="56" y="33" width="7" height="53"/><rect x="86" y="25" width="7" height="61"/><rect x="116" y="17" width="7" height="69"/><rect x="146" y="6" width="7" height="80"/>
        <text x="25" y="36">16.9</text><text x="55" y="31">18.5</text><text x="85" y="23">21.3</text><text x="115" y="15">24.1</text><text x="145" y="4">28.0</text>
        <text x="22" y="93">2012-13</text><text x="52" y="93">2013-14</text><text x="82" y="93">2014-15</text><text x="112" y="93">2015-16</text><text x="142" y="93">2016-17</text>
      </g>
    </svg>
    <div class="fill" style="left:40px;top:114px;width:110px;height:9px;background:var(--green);border-radius:6px;font-size:3.6px;color:#fff;text-align:center;padding-top:2px">Sourced from the Australian Bureau of Statistics</div>
  </div>
  <div class="fill head" style="right:6px;top:345px;color:var(--ink);font-size:7.5px;font-weight:500">Business Opportunities</div>
  <div class="footer"><span class="web">www.kestreladvisory.com.au</span><span class="tab">Page 4</span></div>
</section>

<section class="page c1 r2">
  <div class="fill" style="left:0;top:0;width:104px;height:364px;background:var(--blue)"></div>
  <div class="fill" style="left:8px;top:8px;width:92px;height:62px;background:linear-gradient(135deg,#c96b3a,#e8dcc4)" role="img" aria-label="Stack of books"></div>
  <div class="fill" style="left:8px;top:90px;width:92px;height:62px;background:linear-gradient(135deg,#d8c7b0,#f1d24a)" role="img" aria-label="Students on campus"></div>
  <div class="fill" style="left:8px;top:176px;width:92px;height:62px;background:linear-gradient(135deg,#2a3a55,#b8c5d6)" role="img" aria-label="Student writing in class"></div>
  <div class="fill" style="left:8px;top:258px;width:92px;height:62px;background:linear-gradient(135deg,#e9eef2,#3d8b5c)" role="img" aria-label="Graduation cap on a notebook"></div>
  <div class="body">
    <div class="feature" style="top:14px"><h4>Growing Destination</h4><p>Australia is currently the third most popular destination for international students in the English-speaking world, behind the United States and the UK. Many students choose to study here because of the cultural diversity, friendly natives, and high quality of education.</p></div>
    <div class="feature" style="top:70px"><h4>Global Recognition</h4><p>Schools and employers all over the world recognise degrees from Australian schools. Graduates from Australian schools are highly sought after due to the impressive international reputation of the Australian education system.</p></div>
    <div class="feature" style="top:118px"><h4>Cost of Living</h4><p>Living expenses and tuition costs are considerably lower in Australia than they are in the United States and United Kingdom. International students are able to work part time while they study, allowing them to offset their living costs.</p></div>
    <div class="feature" style="top:166px"><h4>Diversity of Education</h4><p>Institutions in Australia offer a wide variety of courses and degrees, so international students can easily find the school and field that are right for them. Students can choose between University, Vocational Education, and English language training.</p></div>
    <div class="feature" style="top:222px"><h4>Work</h4><p>Students visiting the country are allowed to work up to 20 hours per week while they are studying in Australia. This is a great opportunity for students who want to earn money to help with living expenses and gain work experience in their field of interest.</p></div>
  </div>
  <div class="quote"><b>'AUSTRALIAN ADVANTAGE'</b><span>- Australia Ranked Third Most Popular Destination for International Students</span></div>
  <div class="footer"><span class="web">www.kestreladvisory.com.au</span><span class="tab">Page 5</span></div>
</section>

<section class="page c2 r2">
  <div class="fill" style="left:0;top:0;width:272px;height:188px;background:var(--blue)"></div>
  <div class="body white fill" style="left:8px;top:22px;width:150px;font-size:4.2px">
    <ul class="bullets">
      <li>In 2017, The Higher education sector had the largest share of enrolments and commencements (43.8% and 32.9% respectively) in 2017.</li>
      <li>The VET sector accounted for 27.2% of total enrolments and 30.2% of total commencements in 2017. Enrolments and commencements in the sector increased by 16.7% and 16.1% respectively. China was the most largest source country for enrolments with 8.5%, followed by the Republic of Korea (8.1%) and Thailand (8.0%).</li>
      <li>The English Language Intensive Courses for Overseas Students (ELICOS) sector accounted for 16.4% of total enrolments and 25.9% of total commencements in 2017. Enrolments and commencements grew by 3.4% and 2.9% respectively. China was the largest ELICOS market in the period with 29.3% share of enrolments, Brazil with 11.7% was the second largest nationality for ELICOS enrolments followed by Colombia (8.3%) and Thailand (6.6%).</li>
    </ul>
  </div>
  <div class="label-box" style="left:160px;top:50px;width:112px">International<br>Student Data</div>
  <div class="fill" style="left:12px;top:196px;width:250px">
    <table class="data">
      <tr><th>Sector</th><th>2016</th><th>2017</th><th>Growth</th><th>2016</th><th>2017</th><th>Growth</th></tr>
      <tr><td>Higher Education</td><td>305,946</td><td>350,472</td><td>14.7%</td><td>131,125</td><td>149,943</td><td>14.3%</td></tr>
      <tr><td>VET</td><td>186,510</td><td>217,696</td><td>16.7%</td><td>118,202</td><td>137,405</td><td>16.1%</td></tr>
      <tr><td>ELICOS</td><td>150,272</td><td>155,448</td><td>3.4%</td><td>124,447</td><td>127,806</td><td>2.9%</td></tr>
      <tr><td>Schools</td><td>23,270</td><td>25,762</td><td>10.7%</td><td>12,371</td><td>13,486</td><td>9.0%</td></tr>
      <tr><td>Non-award</td><td>44,104</td><td>49,993</td><td>13.1%</td><td>35,775</td><td>37,864</td><td>6.5%</td></tr>
      <tr class="total"><td>Total</td><td>709,805</td><td>799,371</td><td>12.7%</td><td>411,070</td><td>455,280</td><td>10.9%</td></tr>
    </table>
    <table class="data" style="margin-top:4px">
      <tr><th>Nationality</th><th>2016</th><th>2017</th><th>Growth</th><th>Share</th><th>Nationality</th><th>2017</th><th>Rank</th></tr>
      <tr><td>China</td><td>191,731</td><td>231,191</td><td>18.5%</td><td>28.9%</td><td>Colombia</td><td>21,638</td><td>9</td></tr>
      <tr><td>India</td><td>77,861</td><td>87,615</td><td>12.6%</td><td>11.0%</td><td>Taiwan</td><td>18,227</td><td>10</td></tr>
      <tr><td>Brazil</td><td>25,347</td><td>35,030</td><td>24.4%</td><td>4.4%</td><td>Indonesia</td><td>17,804</td><td>11</td></tr>
      <tr><td>Nepal</td><td>22,884</td><td>35,423</td><td>56.2%</td><td>4.4%</td><td>Sri Lanka</td><td>10,528</td><td>12</td></tr>
      <tr><td>Malaysia</td><td>26,295</td><td>32,999</td><td>16.3%</td><td>4.1%</td><td>Spain</td><td>7,729</td><td>13</td></tr>
      <tr class="total"><td>All nationalities</td><td>709,805</td><td>799,371</td><td>12.7%</td><td>100%</td><td>Bangladesh</td><td>6,565</td><td>14</td></tr>
    </table>
  </div>
  <div class="fill" style="left:60px;top:332px;width:152px;height:9px;background:var(--blue);border-radius:6px;font-size:3.8px;color:#fff;text-align:center;padding-top:2px">Sourced from The Department of Education and Training Australia</div>
  <div class="footer"><span class="web">www.kestreladvisory.com.au</span><span class="tab">Page 6</span></div>
</section>

<section class="page c3 r2">
  <div class="fill" style="left:0;top:0;width:150px;height:150px;background:var(--blue)"></div>
  <div class="fill" style="left:8px;top:10px;width:134px;height:134px;background:linear-gradient(135deg,#eef4fb,#c9d9ef 60%,#f5c36b)" role="img" aria-label="Infographic of international student numbers, January to December 2017"></div>
  <div class="label-box" style="left:160px;top:50px;width:112px">International<br>Student Data</div>
  <div class="body fill" style="left:10px;top:160px;width:225px;font-size:4.2px">In 2017, there were 799,371 enrolments generated by 624,001 full-fee paying international students in Australia on a student visa. This represented a 12.7% increase on 2016 and compared with an average annual enrolments growth rate of 4.4% per year over the preceding ten years.</div>
  <svg class="fill" style="left:10px;top:188px" width="225" height="150" viewBox="0 0 225 150">
    <text x="60" y="6" font-size="3.5" font-family="Open Sans">International Student Enrolments in Australia 1994-2017</text>
    <g stroke="#ccc" stroke-width=".4"><path d="M16 20H222M16 45H222M16 70H222M16 95H222M16 120H222"/></g>
    <path d="M16 10V134H222" stroke="#333" stroke-width=".6" fill="none"/>
    <g fill="#2b3a8f">
      <rect x="20" y="126" width="3" height="8"/><rect x="28" y="125" width="3" height="9"/><rect x="36" y="123" width="3" height="11"/><rect x="44" y="121" width="3" height="13"/><rect x="52" y="118" width="3" height="16"/><rect x="60" y="115" width="3" height="19"/><rect x="68" y="111" width="3" height="23"/><rect x="76" y="107" width="3" height="27"/><rect x="84" y="102" width="3" height="32"/><rect x="92" y="98" width="3" height="36"/><rect x="100" y="95" width="3" height="39"/><rect x="108" y="92" width="3" height="42"/><rect x="116" y="86" width="3" height="48"/><rect x="124" y="78" width="3" height="56"/><rect x="132" y="70" width="3" height="64"/><rect x="140" y="62" width="3" height="72"/><rect x="148" y="66" width="3" height="68"/><rect x="156" y="72" width="3" height="62"/><rect x="164" y="76" width="3" height="58"/><rect x="172" y="74" width="3" height="60"/><rect x="180" y="68" width="3" height="66"/><rect x="188" y="60" width="3" height="74"/><rect x="196" y="50" width="3" height="84"/><rect x="204" y="36" width="3" height="98"/>
    </g>
    <g fill="var(--blue)">
      <rect x="23" y="128" width="2" height="6"/><rect x="31" y="127" width="2" height="7"/><rect x="39" y="126" width="2" height="8"/><rect x="47" y="124" width="2" height="10"/><rect x="55" y="122" width="2" height="12"/><rect x="63" y="120" width="2" height="14"/><rect x="71" y="116" width="2" height="18"/><rect x="79" y="112" width="2" height="22"/><rect x="87" y="106" width="2" height="28"/><rect x="95" y="100" width="2" height="34"/><rect x="103" y="96" width="2" height="38"/><rect x="111" y="92" width="2" height="42"/><rect x="119" y="88" width="2" height="46"/><rect x="127" y="76" width="2" height="58"/><rect x="135" y="64" width="2" height="70"/><rect x="143" y="54" width="2" height="80"/><rect x="151" y="60" width="2" height="74"/><rect x="159" y="70" width="2" height="64"/><rect x="167" y="72" width="2" height="62"/><rect x="175" y="68" width="2" height="66"/><rect x="183" y="62" width="2" height="72"/><rect x="191" y="52" width="2" height="82"/><rect x="199" y="40" width="2" height="94"/><rect x="207" y="20" width="2" height="114"/>
    </g>
    <g font-size="3" font-family="Open Sans" fill="#333"><text x="40" y="30">Higher Education</text><text x="40" y="35">VET</text><text x="40" y="40">ELICOS</text><text x="40" y="45">Schools</text><text x="40" y="50">Non-award</text></g>
    <text x="16" y="142" font-size="3" font-family="Open Sans" fill="#333">Note: There is a break in series between 2001 and 2002</text>
  </svg>
  <div class="fill" style="left:240px;top:150px;width:22px;height:210px;background:var(--blue)">
    <div style="position:absolute;left:7px;top:6px;writing-mode:vertical-rl;font-size:4.5px;color:#fff">Sourced from The Department of Education and Training Australia</div>
  </div>
  <div class="footer"><span class="web">www.kestreladvisory.com.au</span><span class="tab">Page 7</span></div>
</section>

<section class="page c4 r2" style="background:var(--blue)">
  <div class="fill" style="left:0;top:0;width:272px;height:160px;background:linear-gradient(135deg,#5a4a3c,#2f3b3a 55%,#c8b89a)" role="img" aria-label="Chalkboard reading Continuing Education with books and pencils"></div>
  <div class="fill" style="left:140px;top:125px;width:102px;height:102px;border-radius:50%;border:3px solid #fff;background:radial-gradient(circle,#f2d7b3,#b47a52)" role="img" aria-label="Students studying together around a table, seen from above"></div>
  <div class="fill head" style="left:14px;top:182px;font-size:12.5px;font-weight:400">International Education<br>Industry Outlook<br>by 2025</div>
  <ul class="bullets ticks body white fill" style="left:8px;top:252px;width:254px;font-size:4.4px">
    <li>Australia's onshore international education sector is forecast to grow from 650,000 enrolments today to 940,000 by 2025 (which equates to a compounding annual growth rate of 3.8 per cent).</li>
    <li>The international education sector's contribution to export earnings is expected to almost double to in excess of $33 billion by 2025.</li>
    <li>The top eight source markets for onshore international learner enrolments across all sectors in 2025 are expected to be China, India, Vietnam, Thailand, Nepal, Malaysia, Brazil and South Korea. Much of the growth in onshore learner enrolments will be driven by Asia – in particular China, India, Nepal, Vietnam and Thailand.</li>
  </ul>
  <div class="footer"><span class="web">www.kestreladvisory.com.au</span><span class="tab">Page 8</span></div>
</section>

<section class="page c1 r3" style="background:var(--blue)">
  <div class="fill" style="left:0;top:0;width:272px;height:240px;background:linear-gradient(180deg,#2e2e2e,#9c9c9c 55%,var(--blue))" role="img" aria-label="Black and white photo of a teacher speaking to a class"></div>
  <div class="fill head" style="left:14px;top:210px;font-size:15px;font-weight:400">International Education Industry<br>Outlook by 2025</div>
  <div class="fill" style="left:120px;top:235px;width:140px;height:1px;background:var(--yellow)"></div>
  <ul class="bullets ticks body white fill" style="left:14px;top:254px;width:248px;font-size:4.3px">
    <li>Over the period to 2025, the fastest growing sectors in onshore international education are expected to be higher education and VET (in percentage terms). By 2025, these two sectors are expected to account for 72 per cent of all onshore international learner enrolments.</li>
    <li>China is set to remain Australia's largest source market for onshore enrolments in 2025 and is expected to occupy the largest number of higher education, schooling and ELICOS enrolments. The largest number of VET onshore enrolments in 2025 are forecast to come from India (16 per cent), Thailand (eight per cent) and South Korea (seven per cent).</li>
  </ul>
  <div class="fill" style="left:0;top:322px;width:272px;height:42px;background:linear-gradient(180deg,transparent,#1f86bd)" role="img" aria-label="Row of raised hands giving thumbs up"></div>
  <div class="footer"><span class="web">www.kestreladvisory.com.au</span><span class="tab">Page 9</span></div>
</section>

<section class="page c2 r3">
  <div class="fill" style="left:0;top:0;width:272px;height:364px;background:linear-gradient(180deg,#3e6f99,#7fa3bf 35%,#f0c89a 62%,#9a7a60 85%,#5a4a42)" role="img" aria-label="Child on a tall stack of books looking through a telescope over a city at sunset"></div>
  <div class="fill wordmark" style="right:10px;top:14px;color:var(--yellow);font-size:16px">Kestrel Advisory</div>
  <div class="body white fill" style="left:10px;top:46px;width:252px;font-size:6.5px;line-height:1.35">Kestrel Advisory has a range of private International Education Colleges for sale delivering qualifications in the Hospitality, Building and Construction, IT, Accounting, Management, Health Services and English Language which have returns from 20-25% per annum.</div>
  <div class="footer"><span class="web">www.kestreladvisory.com.au</span><span class="tab">Page 10</span></div>
</section>

<section class="page c3 r3 contact">
  <div class="fill head" style="left:0;top:30px;width:272px;text-align:center;color:var(--ink);font-size:10.5px;font-weight:500">PLEASE CONTACT US FOR FURTHER INFORMATION</div>
  <div class="fill" style="left:0;top:60px;width:272px;height:304px;background:var(--blue)"></div>
  <div class="fill" style="left:8px;top:72px;width:97px;height:90px;background:linear-gradient(135deg,#d9b15a,#6a7d3a);border:1px solid #fff" role="img" aria-label="Portrait photo of Daniel Reyes"></div>
  <div class="fill" style="left:118px;top:108px">
    <h5>Daniel Reyes</h5><div class="role">OIEC / Director of Sales &amp; Leasing</div>
    <div class="line"><svg width="5" height="5" viewBox="0 0 10 10"><circle cx="5" cy="5" r="5" fill="var(--green)"/><path d="M3 3l1 0 1 2-1 1 2 2 1-1 2 1v1q-3 1-6-3z" fill="#fff"/></svg>+61 400 100 200</div>
    <div class="line"><svg width="5" height="5" viewBox="0 0 10 10"><rect y="2" width="10" height="7" fill="var(--yellow)"/><path d="M0 2l5 4 5-4" stroke="var(--blue)" fill="none"/></svg>daniel.reyes@kestreladvisory.com.au</div>
  </div>
  <div class="fill" style="left:8px;top:198px;width:97px;height:90px;background:var(--yellow);border:1px solid #fff"></div>
  <div class="fill" style="left:118px;top:234px">
    <h5>Omar Haddad</h5><div class="role">Business Development Manager (Education/Training<br>Organisation)</div>
    <div class="line"><svg width="5" height="5" viewBox="0 0 10 10"><circle cx="5" cy="5" r="5" fill="var(--green)"/><path d="M3 3l1 0 1 2-1 1 2 2 1-1 2 1v1q-3 1-6-3z" fill="#fff"/></svg>+61 400 300 400</div>
    <div class="line"><svg width="5" height="5" viewBox="0 0 10 10"><rect y="2" width="10" height="7" fill="var(--yellow)"/><path d="M0 2l5 4 5-4" stroke="var(--blue)" fill="none"/></svg>omar.haddad@kestreladvisory.com.au</div>
  </div>
  <div class="footer"><span class="web">www.kestreladvisory.com.au</span><span class="tab">Page 11</span></div>
</section>

<section class="page c4 r3" style="background:var(--blue)">
  <div class="fill" style="left:0;top:0;width:272px;height:244px;background:linear-gradient(135deg,#f2e23a,#8c8320 55%,#e9dc5a)" role="img" aria-label="Yellow-toned photo of hands typing on a laptop showing online learning"></div>
  <div class="fill wordmark" style="left:0;top:262px;width:272px;text-align:center;font-size:13px;color:#fff">Kestrel Advisory</div>
  <svg class="fill" style="left:131px;top:292px" width="10" height="12" viewBox="0 0 10 12"><path d="M5 12C1 7 0 5.5 0 4.5a5 4.5 0 0 1 10 0C10 5.5 9 7 5 12z" fill="var(--yellow)"/><circle cx="5" cy="4.5" r="1.8" fill="var(--blue)"/></svg>
  <div class="fill" style="left:0;top:308px;width:272px;text-align:center;font-size:5px;font-weight:700;color:#fff">Level 4, 88 Harbour Lane Melbourne</div>
  <svg class="fill" style="left:131px;top:320px" width="10" height="10" viewBox="0 0 10 10"><circle cx="5" cy="5" r="4.5" fill="none" stroke="var(--yellow)"/><path d="M.5 5h9M5 .5v9M2 2.5q3 1.5 6 0M2 7.5q3-1.5 6 0" stroke="var(--yellow)" fill="none" stroke-width=".6"/></svg>
  <div class="fill" style="left:0;top:334px;width:272px;text-align:center;font-size:5px;font-weight:700;color:#fff">www.kestreladvisory.com.au</div>
</section>

</body>
</html>
```